A revolutionary website for a revolutionary construction company

I am looking for inspirations... please help me and read the attached brief

I would like to achieve a website design that is modern, premium dynamic and drives emotions. I do not want a design that can be found on a normal template. Having that said, I would also like the utilisation of Illustrations that are relation to the company’s services…. Also would like to have illustrations dynamic when you navigate on them. So a young, dynamic and parallax design website that will show off these requirements. Also to add trust, with all pages designed.

please see attachements.
Updates

Low design quality

Target Market(s)

Please read brief

Number of Pages Required

5+ page

Font styles to use
Other font styles liked:
• Futura

Requirements
Must have
• Please read brief - colours to be matching logo colours
Nice to have
Should not have

```html
<!DOCTYPE html>
<html lang="en">
<head>
<meta charset="utf-8">
<title>Ironvale Build — Constructed Beyond Belief</title>
<link rel="stylesheet" href="https://fonts.googleapis.com/css2?family=Montserrat:wght@300;400;600;700&family=Open+Sans:wght@400;600&display=swap">
<style>
:root{
  --crimson:#a00a3e;
  --crimson-dark:#7d0730;
  --crimson-deep:#5c0522;
  --orange:#ff7b06;
  --orange-ring:#e0521a;
  --stone:#5f5858;
  --stone-circle:#5b5455;
  --night:#2e2a2b;
  --white:#ffffff;
  --muted:#e8dfe2;
  --head:'Montserrat',sans-serif;
  --body:'Open Sans',Arial,sans-serif;
}
*{box-sizing:border-box;margin:0;padding:0}
html,body{width:1200px;height:3060px;overflow:hidden}
body{position:relative;background:var(--crimson);color:var(--white);font-family:var(--body)}
.abs{position:absolute}
.shapes{position:absolute;left:0;top:0}

/* header */
.brand{position:absolute;left:173px;top:11px;display:flex;align-items:center;gap:10px}
.brand-dot{width:74px;height:74px;border-radius:50%;background:var(--white)}
.brand-name{font-family:var(--head);font-weight:700;font-size:15px;letter-spacing:1px;color:var(--white)}
.nav{position:absolute;top:35px;left:379px;display:flex;font-family:var(--head);font-size:11.5px;font-weight:600;letter-spacing:.4px}
.nav a{color:var(--white);text-decoration:none;position:absolute;white-space:nowrap}
.nav a.active::after{content:"";position:absolute;left:0;right:0;top:23px;height:2px;background:var(--white)}
.phone{position:absolute;left:877px;top:33px;font-family:var(--head);font-size:14px;font-weight:600}
.phone b{font-weight:700;font-size:15px}
.btn{position:absolute;display:flex;align-items:center;justify-content:center;background:var(--orange);color:var(--white);font-family:var(--head);font-weight:700;letter-spacing:1.2px;border-radius:20px;box-shadow:0 0 0 2px var(--crimson),0 0 0 3.5px var(--orange-ring)}

/* hero */
.hero-kicker{left:645px;top:258px;font-family:var(--head);font-weight:600;font-size:17px}
.hero-title{left:643px;top:276px;font-family:var(--head);font-weight:700;font-size:53px;letter-spacing:.5px;line-height:1.15}
.hero-text{left:647px;top:348px;width:365px;font-size:14px;line-height:17px}

/* section heads */
.center-head{left:0;width:1200px;text-align:center;font-family:var(--head);font-weight:700}
.mini-brand{left:0;width:1200px;text-align:center;font-family:var(--head);font-weight:700;font-size:12px;letter-spacing:2px}
.center-text{left:0;width:1200px;text-align:center;font-size:14px;line-height:18px}

/* services */
.service{position:absolute;width:220px;text-align:center;top:812px}
.service-ring{width:110px;height:110px;border-radius:50%;border:2px solid var(--white);margin:0 auto;display:flex;align-items:center;justify-content:center}
.service-ring.is-current{background:var(--stone-circle);border-color:var(--stone-circle)}
.service-label{margin-top:28px;font-family:var(--head);font-weight:600;font-size:12.5px;letter-spacing:1.3px}
.rule{left:173px;top:1003px;width:852px;height:1px;background:rgba(255,255,255,.55)}

/* story */
.story-title{left:173px;font-family:var(--head);font-weight:700;font-size:36px;line-height:43px}
.underline{height:2px;width:64px;background:var(--white)}
.story-text{font-size:11.3px;line-height:17px}

/* numbers */
.numbers-title{left:173px;top:1853px;font-family:var(--head);font-weight:700;font-size:26px}
.stat{position:absolute;top:1913px;width:176px;height:164px;padding:12px 0 0 0}
.stat.is-focus{background:var(--crimson)}
.stat-value{font-family:var(--head);font-weight:300;font-size:27px;margin-top:10px}
.stat-text{font-size:11.3px;line-height:17px;margin-top:6px}

/* projects */
.project{position:absolute;top:2447px;width:272px;height:220px;background:var(--white);padding:6px}
.project svg{display:block}
.pager{left:0;width:1200px;top:2718px;display:flex;justify-content:center;align-items:center;gap:14px;font-family:var(--head);font-weight:600;font-size:17px}

/* footer */
.footer{left:0;top:2827px;width:1200px;height:233px;background:var(--night)}
.foot-head{position:absolute;top:30px;font-family:var(--head);font-weight:700;font-size:12.5px}
.foot-text{position:absolute;top:58px;font-size:10.8px;line-height:14.5px;color:var(--muted)}
.foot-links{position:absolute;top:58px;font-size:10.8px;line-height:19.5px;color:var(--muted);list-style:none}
.social{position:absolute;top:56px;left:822px;display:flex;gap:8px}
.social span{width:23px;height:23px;border-radius:50%;background:var(--crimson);display:block}
.foot-rule{position:absolute;left:0;top:187px;width:1200px;height:1px;background:rgba(255,255,255,.18)}
.foot-base{position:absolute;top:203px;font-size:10.5px;color:var(--muted)}
</style>
</head>
<body>

<!-- background shapes -->
<svg class="shapes" width="1200" height="3060" viewBox="0 0 1200 3060" aria-hidden="true">
  <defs>
    <linearGradient id="dusk" x1="0" y1="0" x2="0" y2="1">
      <stop offset="0" stop-color="#6f6e70"/>
      <stop offset=".3" stop-color="#d39a3a"/>
      <stop offset=".55" stop-color="#e58a1a"/>
      <stop offset="1" stop-color="#7c2b3a"/>
    </linearGradient>
    <linearGradient id="worker" x1="0" y1="0" x2="1" y2="1">
      <stop offset="0" stop-color="#c9b9ae"/>
      <stop offset=".45" stop-color="#3b4560"/>
      <stop offset=".7" stop-color="#e86a1e"/>
      <stop offset="1" stop-color="#2b2c3a"/>
    </linearGradient>
    <linearGradient id="sparks" x1="0" y1="0" x2="1" y2="1">
      <stop offset="0" stop-color="#3fa2c4"/>
      <stop offset=".4" stop-color="#14202e"/>
      <stop offset=".75" stop-color="#7a1a2a"/>
      <stop offset="1" stop-color="#a00a3e"/>
    </linearGradient>
  </defs>
  <rect x="0" y="1813" width="1200" height="310" fill="#5f5858"/>
  <polygon points="921,1118 1091,1118 1008,1198 921,1198" fill="#5c0522" opacity=".0"/>
  <polygon points="921,1118 1091,1118 980,1240 850,1240" fill="#7d0730"/>
</svg>

<!-- hero photograph -->
<svg class="abs" style="left:0;top:0" width="796" height="832" viewBox="0 0 796 832" role="img" aria-label="City skyline with a tall tower and cranes at golden sunset">
  <polygon points="0,0 796,0 0,832" fill="url(#dusk)"/>
  <polygon points="0,540 280,540 0,832" fill="#a00a3e" opacity=".55"/>
</svg>

<!-- worker photograph -->
<svg class="abs" style="left:558px;top:1198px" width="642" height="615" viewBox="0 0 642 615" role="img" aria-label="Construction worker in an orange hard hat carrying a heavy pipe">
  <polygon points="535,0 642,0 642,615 0,615" fill="url(#worker)"/>
  <polygon points="430,0 535,0 0,615 0,480" fill="#6e0b25" opacity=".85"/>
</svg>

<!-- welding photograph -->
<svg class="abs" style="left:0;top:2123px" width="493" height="693" viewBox="0 0 493 693" role="img" aria-label="Welder's torch throwing bright blue light and orange sparks">
  <polygon points="0,0 493,0 0,693" fill="url(#sparks)"/>
</svg>

<!-- header -->
<div class="brand"><span class="brand-dot"></span></div>
<nav class="nav">
  <a class="active" style="left:0">HOME</a>
  <a style="left:66px">ABOUT US</a>
  <a style="left:153px">SERVICES</a>
  <a style="left:239px">PROJECTS</a>
  <a style="left:324px">CONTACT US</a>
</nav>
<div class="phone">+1(555) <b>410-27-36</b></div>
<div class="btn" style="left:860px;top:66px;width:164px;height:31px;font-size:11.5px">CALL US TODAY</div>

<!-- hero -->
<div class="abs hero-kicker">Constructed</div>
<h1 class="abs hero-title">Beyond Belief</h1>
<p class="abs hero-text">Lorem ipsum dolor sit amet, consectetur adipiscing elit, sed do eiusmod tempor incididunt ut labore et dolore magna aliqua.</p>
<div class="btn" style="left:648px;top:430px;width:166px;height:32px;font-size:11px">FIND OUT MORE</div>

<!-- services -->
<div class="abs mini-brand" style="top:646px">IRONVALE BUILD</div>
<h2 class="abs center-head" style="top:677px;font-size:36px">Services we provide</h2>
<p class="abs center-text" style="top:735px">Ut enim ad minim veniam, quis nostrud exercitation ullamco laboris<br>nisi ut aliquip ex ea commodo consequat.</p>

<div class="service" style="left:167px">
  <div class="service-ring">
    <svg width="50" height="50" viewBox="0 0 50 50" fill="none" stroke="#fff" stroke-width="2" stroke-linejoin="round" aria-hidden="true">
      <path d="M6 24 L25 7 L44 24"/><path d="M11 20 V44 H39 V20"/><path d="M22 40 L31 22 L35 24 L26 42 L21 44 Z"/>
    </svg>
  </div>
  <div class="service-label">DESIGN AND CONSTRUCT</div>
</div>
<div class="service" style="left:375px">
  <div class="service-ring is-current">
    <svg width="50" height="50" viewBox="0 0 50 50" fill="none" stroke="#fff" stroke-width="2" stroke-linejoin="round" aria-hidden="true">
      <path d="M14 20 C14 10 36 10 36 20 Z"/><path d="M11 20 H39"/><path d="M25 9 V14"/><path d="M10 44 C10 34 16 30 25 30 C34 30 40 34 40 44"/><path d="M19 30 V44 M31 30 V44"/>
    </svg>
  </div>
  <div class="service-label">CONSTRUCTION</div>
</div>
<div class="service" style="left:587px">
  <div class="service-ring">
    <svg width="50" height="50" viewBox="0 0 50 50" fill="none" stroke="#fff" stroke-width="2" stroke-linejoin="round" aria-hidden="true">
      <rect x="8" y="9" width="26" height="34" rx="2"/><rect x="15" y="6" width="12" height="6" rx="1"/><path d="M13 20 l3 3 5-5 M13 30 l3 3 5-5 M24 21 H29"/><circle cx="36" cy="36" r="9"/><path d="M36 31 V36 H40"/>
    </svg>
  </div>
  <div class="service-label">PROJECT MANAGEMENT</div>
</div>
<div class="service" style="left:817px">
  <div class="service-ring">
    <svg width="50" height="50" viewBox="0 0 50 50" fill="none" stroke="#fff" stroke-width="2" aria-hidden="true">
      <circle cx="25" cy="28" r="16"/><circle cx="25" cy="28" r="11"/><path d="M21 8 H29 M25 8 V12 M39 12 l3-3"/>
      <text x="25" y="32" text-anchor="middle" fill="#fff" stroke="none" font-family="Montserrat,sans-serif" font-size="11" font-weight="700">24</text>
    </svg>
  </div>
  <div class="service-label">24-HR SERVICE CALLS</div>
</div>
<div class="abs rule"></div>

<!-- story -->
<h2 class="abs story-title" style="top:1083px">We build your dreams</h2>
<div class="abs underline" style="left:173px;top:1143px"></div>
<p class="abs story-text" style="left:173px;top:1181px;width:275px">Lorem ipsum dolor sit amet, consectetur adipiscing elit, sed do eiusmod tempor incididunt ut labore et dolore magna aliqua. Ut enim ad minim veniam, quis nostrud exercitation ullamco laboris nisi ut aliquip ex ea commodo consequat. Duis aute irure dolor in reprehenderit in voluptate velit esse cillum dolore eu fugiat nulla pariatur. Excepteur sint occaecat cupidatat non proident, sunt in culpa qui officia deserunt mollit anim id est laborum.</p>
<p class="abs story-text" style="left:481px;top:1181px;width:285px">The passage experienced a surge in popularity during the 1960s when Typeframe used it on their dry-transfer sheets, and again during the 90s as desktop publishers bundled the text with their software. Today it's seen all around the web; on templates, websites, and stock designs. Use our generator to get your own, or read on for the authoritative history of lorem ipsum. A practice not without controversy, laying out pages with meaningless filler text can.</p>
<h2 class="abs story-title" style="top:1372px">Managing through<br>changing time</h2>
<div class="abs underline" style="left:173px;top:1479px"></div>
<p class="abs story-text" style="left:173px;top:1508px;width:338px">Lorem ipsum dolor sit amet, consectetur adipiscing elit, sed do eiusmod tempor incididunt ut labore et dolore magna aliqua. Ut enim ad minim veniam, quis nostrud exercitation ullamco laboris nisi ut aliquip ex ea commodo consequat. Duis aute irure dolor in reprehenderit in voluptate velit esse cillum dolore eu fugiat nulla pariatur. Excepteur sint occaecat cupidatat non proident, sunt in culpa qui officia deserunt mollit anim id est laborum.</p>
<div class="btn" style="left:172px;top:1684px;width:162px;height:31px;font-size:11px">FIND OUT MORE</div>

<!-- numbers -->
<h2 class="abs numbers-title">Our business in numbers</h2>
<div class="stat" style="left:174px">
  <svg width="38" height="34" viewBox="0 0 38 34" fill="none" stroke="#fff" stroke-width="2" aria-hidden="true"><circle cx="10" cy="6" r="4"/><path d="M4 30 L10 14 L18 20 L14 30 M18 20 L24 12"/><path d="M20 32 L28 16 L36 32 Z"/></svg>
  <div class="stat-value">£ 1.1 bn</div>
  <div class="stat-text">revenue and a major<br>contractor across the UK</div>
</div>
<div class="stat is-focus" style="left:383px;padding-left:26px">
  <svg width="42" height="34" viewBox="0 0 42 34" fill="none" stroke="#fff" stroke-width="2" aria-hidden="true"><circle cx="10" cy="9" r="5"/><circle cx="21" cy="7" r="5"/><circle cx="32" cy="9" r="5"/><path d="M2 26 C2 18 18 18 18 26 M13 24 C13 15 29 15 29 24 M24 26 C24 18 40 18 40 26"/></svg>
  <div class="stat-value">3,000</div>
  <div class="stat-text">passionate and talented<br>employees across the UK</div>
</div>
<div class="stat" style="left:643px;width:200px">
  <svg width="34" height="34" viewBox="0 0 34 34" fill="none" stroke="#fff" stroke-width="2" aria-hidden="true"><path d="M3 8 L17 2 L31 8 L17 14 Z"/><path d="M9 11 V16 C9 24 25 24 25 16 V11"/><path d="M6 33 C6 26 28 26 28 33"/></svg>
  <div class="stat-value">8.2 %</div>
  <div class="stat-text">of our people are apprentices,<br>graduates or trainees</div>
</div>
<div class="stat" style="left:893px;width:200px">
  <svg width="36" height="34" viewBox="0 0 36 34" fill="none" stroke="#fff" stroke-width="2" aria-hidden="true"><path d="M5 26 C5 12 31 12 31 26 Z"/><path d="M2 28 H34"/><path d="M15 13 V26 M21 13 V26"/></svg>
  <div class="stat-value">0.07</div>
  <div class="stat-text">AFR reflecting our<br>commitment to excellent<br>health and safety</div>
</div>

<!-- projects -->
<div class="abs mini-brand" style="top:2252px">IRONVALE BUILD</div>
<h2 class="abs center-head" style="top:2283px;font-size:36px">Our Latest Projects</h2>
<div class="abs underline" style="left:568px;top:2337px"></div>
<p class="abs center-text" style="top:2351px;font-size:11.6px;line-height:18px">Lorem ipsum dolor sit amet, consectetur adipiscing elit, sed do eiusmod<br>tempor incididunt ut labore et dolore magna aliqua.</p>

<div class="project" style="left:173px">
  <svg width="260" height="208" viewBox="0 0 260 208" role="img" aria-label="Modern white and timber villa with glass balconies"><defs><linearGradient id="p1" x1="0" y1="0" x2="0" y2="1"><stop offset="0" stop-color="#8fb7de"/><stop offset=".55" stop-color="#d9d8d6"/><stop offset="1" stop-color="#5b5450"/></linearGradient></defs><rect width="260" height="208" fill="url(#p1)"/></svg>
</div>
<div class="project" style="left:464px">
  <svg width="260" height="208" viewBox="0 0 260 208" role="img" aria-label="Stone-clad lakeside house in warm evening sunlight"><defs><linearGradient id="p2" x1="0" y1="0" x2="0" y2="1"><stop offset="0" stop-color="#c9c6c0"/><stop offset=".5" stop-color="#5c5550"/><stop offset="1" stop-color="#3a3835"/></linearGradient></defs><rect width="260" height="208" fill="url(#p2)"/></svg>
</div>
<div class="project" style="left:756px">
  <svg width="260" height="208" viewBox="0 0 260 208" role="img" aria-label="Large white manor with a long driveway at dusk"><defs><linearGradient id="p3" x1="0" y1="0" x2="0" y2="1"><stop offset="0" stop-color="#a9b3bd"/><stop offset=".55" stop-color="#6a6963"/><stop offset="1" stop-color="#4d5a3e"/></linearGradient></defs><rect width="260" height="208" fill="url(#p3)"/></svg>
</div>

<div class="abs pager">
  <svg width="14" height="18" viewBox="0 0 14 18" fill="none" stroke="#d7c9cf" stroke-width="3" aria-hidden="true"><path d="M11 2 L4 9 L11 16"/></svg>
  <span>1 / 4</span>
  <svg width="14" height="18" viewBox="0 0 14 18" fill="none" stroke="#d7c9cf" stroke-width="3" aria-hidden="true"><path d="M3 2 L10 9 L3 16"/></svg>
</div>

<!-- footer -->
<footer class="abs footer">
  <div class="foot-head" style="left:173px">About Us</div>
  <p class="foot-text" style="left:173px;width:190px">Lorem ipsum dolor sit amet, conse ctetur adipiscing elit, sed do eiusmod tempor incididunt ut labore et dolore magna aliqua.</p>

  <div class="foot-head" style="left:399px">Our Address</div>
  <p class="foot-text" style="left:399px;width:170px">18 Quarry Lane Avenue<br>Millbrook town, Westland<br><br>Phone: 55502918<br>Email: hello@ironvale.test<br>Office Time: 10AM- 5PM</p>

  <div class="foot-head" style="left:575px">Quick Links</div>
  <ul class="foot-links" style="left:575px"><li>About us</li><li>Our services</li><li>Contact us</li><li>Meet team</li></ul>
  <ul class="foot-links" style="left:678px"><li>Privacy Policy</li><li>Testimonials</li><li>News</li><li>FAQ</li></ul>

  <div class="foot-head" style="left:822px">Follow Us</div>
  <div class="social"><span></span><span></span><span></span></div>

  <div class="foot-rule"></div>
  <div class="foot-base" style="left:173px">Copyright © 2020 Ironvale Build . All Rights Reserved</div>
  <div class="foot-base" style="left:879px">Terms of Use &nbsp;|&nbsp;&nbsp; Privacy Policy</div>
</footer>

</body>
</html>
```